PREMIUM AGENCY High End Business Card - A+++ Designers Wanted

** DO NOT ATTEMPT TO CONTACT ME THROUGH SEARCHING ON ZINTREL OR EMAILING ME THROUGH MY WEBSITE **

I need a fresh, contemporary business card designed using the logo attached (BRONSALK)

I have attached the font for BRONSALK

It must have a premium look and feel. The business card size must be STANDARD size.

You can submit either/both VERTICAL or HORIZONTAL designs.

FRONT: It must have the following sample information on

Paul Ardley
Director Operations
Mobile +61 452 118 906
Email paulardley@bronsalk.com
www.bronsalk.com

The REAR of the business card must have the words

CREATE INSPIRE TOMORROW

as part of the design, in the same font (NEXA) attached.

The words do not need to be in capitals, or on the same line, please design this as you see it best working.

ADDITIONAL INFORMATION
======================

The BRONSALK logo must be on the front of the card

I want Ultraviolet printing on the final design, to enhance either the NAME of the person OR the BRONSALK logo OR the words on the back of the card.

Target Market(s)

Agency, Advertising Agency, Creative, Designers

Industry/Entity Type

Media

Contact Information for Business Card

Design Agency, Contemporary, Premium look and feel, High Quality

Font styles to use
Serif
Sans Serif
Other font styles liked:
• ATTACHED TO PROJECT

Requirements
Must have
• BLACK & WHITE as the primary design, and if you feel there can be a highlighted colour, then this can be used.
• The Logo ICON attached is blue, this colour must not be changed.
• I have attached the partner brand BRONSALK MEDIA incase you need to manipulate the original files.
• ** DO NOT ATTEMPT TO CONTACT ME THROUGH SEARCHING ON ZINTREL OR EMAILING ME THROUGH MY WEBSITE **
Nice to have
• Must be Premium. I have attached some sample designs, that I like that would be a good inspiration for where this can be taken.
• My favourite design is is the KESTRAVUE2-BUSINESSCARD-TEMPLATE
Should not have
• No funny or silly standard / off the shelf designs

```html
<!DOCTYPE html>
<html lang="en">
<head>
<meta charset="utf-8">
<title>Bronsalk Media – Business Card</title>
<link rel="stylesheet" href="https://fonts.googleapis.com/css2?family=Montserrat:wght@300;400;600;700&display=swap">
<style>
  :root {
    --stage: #e7e4df;
    --card-white: #ffffff;
    --card-black: #050505;
    --ink: #111111;
    --ink-soft: #3a3a3a;
    --accent: #29b0d9;
    --rule: #222222;
  }
  * { box-sizing: border-box; margin: 0; padding: 0; }
  html, body { width: 1200px; height: 780px; overflow: hidden; }
  body {
    background: var(--stage);
    font-family: "Montserrat", Arial, sans-serif;
    display: flex;
    align-items: center;
    justify-content: center;
    gap: 60px;
  }
  .card {
    position: relative;
    width: 520px;
    height: 297px;
    border-radius: 14px;
    overflow: hidden;
    box-shadow: 0 10px 26px rgba(0,0,0,0.18);
  }

  /* Front */
  .card-front { background: var(--card-white); color: var(--ink); }
  .brand {
    position: absolute;
    left: 36px;
    top: 58px;
    display: flex;
    align-items: center;
    gap: 14px;
  }
  .brand-dot {
    width: 26px; height: 26px;
    border-radius: 50%;
    background: var(--accent);
  }
  .brand-name {
    font-size: 34px;
    font-weight: 600;
    letter-spacing: 0.02em;
    color: var(--ink);
  }
  .divider {
    position: absolute;
    left: 76px;
    top: 163px;
    width: 250px;
    height: 1px;
    background: var(--rule);
  }
  .person {
    position: absolute;
    left: 338px;
    top: 132px;
  }
  .person-name {
    font-size: 19px;
    font-weight: 700;
    color: var(--accent);
    text-transform: uppercase;
    letter-spacing: -0.01em;
    line-height: 1;
  }
  .person-role {
    margin-top: 5px;
    font-size: 12.5px;
    font-weight: 400;
    color: var(--ink-soft);
  }
  .contacts {
    position: absolute;
    left: 76px;
    top: 192px;
    display: flex;
    align-items: center;
    gap: 10px;
  }
  .contact-icons { display: flex; flex-direction: column; gap: 4px; }
  .contact-icon {
    width: 16px; height: 16px;
    border-radius: 2px;
    background: var(--accent);
    display: flex; align-items: center; justify-content: center;
  }
  .contact-lines {
    font-size: 12.5px;
    line-height: 20px;
    color: var(--ink-soft);
  }
  .website {
    position: absolute;
    right: 30px;
    top: 226px;
    font-size: 12.5px;
    color: var(--ink);
  }
  .accent-band {
    position: absolute;
    left: 0; right: 0; bottom: 0;
    height: 14px;
    background: var(--accent);
  }

  /* Back */
  .card-back {
    background: var(--card-black);
    display: flex;
    align-items: center;
    justify-content: center;
  }
  .tagline {
    text-align: center;
    font-weight: 300;
    font-size: 36px;
    line-height: 1.05;
    letter-spacing: 0.04em;
    color: var(--accent);
    text-transform: uppercase;
  }
</style>
</head>
<body>
  <section class="card card-front" aria-label="Business card front">
    <div class="brand">
      <span class="brand-dot"></span>
      <span class="brand-name">BRONSALK MEDIA</span>
    </div>
    <div class="divider"></div>
    <div class="person">
      <div class="person-name">Paul Ardley</div>
      <div class="person-role">Director Operations</div>
    </div>
    <div class="contacts">
      <div class="contact-icons">
        <span class="contact-icon" aria-label="Mobile">
          <svg width="8" height="11" viewBox="0 0 8 11"><rect x="0.8" y="0.6" width="6.4" height="9.8" rx="1" fill="none" stroke="#fff" stroke-width="1.1"/><circle cx="4" cy="8.7" r="0.7" fill="#fff"/></svg>
        </span>
        <span class="contact-icon" aria-label="Email">
          <svg width="11" height="8" viewBox="0 0 11 8"><rect x="0.6" y="0.6" width="9.8" height="6.8" fill="none" stroke="#fff" stroke-width="1.1"/><path d="M0.8 0.8 L5.5 4.6 L10.2 0.8" fill="none" stroke="#fff" stroke-width="1.1"/></svg>
        </span>
      </div>
      <div class="contact-lines">
        <div>+61 452 118 906</div>
        <div>paulardley@bronsalk.com</div>
      </div>
    </div>
    <div class="website">www.bronsalk.com</div>
    <div class="accent-band"></div>
  </section>

  <section class="card card-back" aria-label="Business card back">
    <p class="tagline">Create<br>Inspire<br>Tomorrow</p>
  </section>
</body>
</html>
```